Personal Finance e-commerce website needs a simple budget design

Hello! I am starting to sell downloadable and printable budget planners, as shown in the attached file, for people to plan ahead on their personal finances. <br/><br/>I want to see a one-page design with similar columns (for example, "Expenses, Budget, and Actual"). I would also like to see the basic formula ("Net Income = Gross income - Total Expenses") somewhere on the design. Finally, I want the design to remain mostly minimalistic and simple for the average person to plan their personal monthly budgets.<br/><br/>However, other than that, the overall design, layout, and colors will be at the graphic designer's choice. If you have any questions for me, please let me know. Thank you for your time!

Industry/Entity Type

Financial Planning

Colors

Designer to choose colors to be used in the design.

Requirements
Must have
• I want to see a one-page design with similar columns (for example, "Expenses, Budget, and Actual").
• I want the design to remain mostly minimalistic and simple for the average person to plan their personal monthly budgets.
Nice to have
• I would also like to see the basic formula ("Net Income = Gross income - Total Expenses") somewhere on the design.

```html
<!DOCTYPE html>
<html lang="en">
<head>
<meta charset="utf-8">
<title>Harlow Penny Basic Monthly Budget</title>
<link href="https://fonts.googleapis.com/css2?family=Raleway:wght@300;400;500;600;700&display=swap" rel="stylesheet">
<style>
:root{
  --backdrop:#dcdcdc;
  --paper:#ffffff;
  --red:#b71f25;
  --red-strong:#eac5c8;
  --red-soft:#f4e5e6;
  --blue:#3ea1d8;
  --blue-strong:#bfdff0;
  --blue-soft:#e3f1f8;
  --green:#8fb03c;
  --green-strong:#dbe3bd;
  --green-soft:#eef0e2;
  --field:#eac5c8;
  --white:#ffffff;
}
*{box-sizing:border-box;margin:0;padding:0}
html,body{width:1200px;height:955px;overflow:hidden;background:var(--backdrop);font-family:"Raleway",sans-serif}
.sheet{position:absolute;left:246px;top:20px;width:707px;height:915px;background:var(--paper)}
.masthead{position:absolute;left:0;top:0;width:100%;height:106px;background:var(--red);color:var(--white)}
.brand{position:absolute;left:40px;top:20px;font-size:27px;font-weight:500;letter-spacing:1px}
.doc-title{position:absolute;left:282px;top:17px;font-size:31px;font-weight:700;letter-spacing:.2px}
.period{position:absolute;right:50px;top:64px;display:flex;align-items:center;gap:8px;font-size:13px;font-weight:700}
.period .field{height:26px;background:var(--field);border-radius:3px}
.period .month{width:161px;margin-right:4px}
.period .year{width:100px}
.ledger{position:absolute;left:50px;top:118px;width:607px}
.ledger-head,.ledger-row{display:grid;grid-template-columns:342px 128px 129px;gap:4px}
.ledger-head{height:42px;margin-bottom:5px}
.col-head{border-radius:3px;color:var(--white);padding:5px 8px 0}
.col-head strong{display:block;font-size:15px;font-weight:600}
.col-head span{display:block;font-size:9.5px;font-weight:300;opacity:.9;margin-top:1px}
.col-head.expense{background:var(--red)}
.col-head.budget{background:var(--blue)}
.col-head.actual{background:var(--green)}
.ledger-rows{display:flex;flex-direction:column;gap:5px}
.ledger-row{height:31px}
.ledger-row div{border-radius:2px}
.ledger-row:nth-child(odd) .c-exp{background:var(--red-strong)}
.ledger-row:nth-child(odd) .c-bud{background:var(--blue-strong)}
.ledger-row:nth-child(odd) .c-act{background:var(--green-strong)}
.ledger-row:nth-child(even) .c-exp{background:var(--red-soft)}
.ledger-row:nth-child(even) .c-bud{background:var(--blue-soft)}
.ledger-row:nth-child(even) .c-act{background:var(--green-soft)}
.formula-band{position:absolute;left:0;bottom:0;width:100%;height:95px;background:var(--red);color:var(--white)}
.formula{position:absolute;left:50px;top:10px;display:flex;align-items:center}
.term{display:flex;align-items:center;gap:9px}
.term svg{width:50px;height:50px;flex:none}
.term strong{display:block;font-size:16px;font-weight:600}
.term span{display:block;font-size:9.5px;font-weight:300;margin-top:1px}
.operator{font-size:26px;font-weight:700;margin:0 14px}
.visit{position:absolute;left:0;width:100%;top:69px;text-align:center;font-size:12.5px;font-weight:600}
</style>
</head>
<body>
<main class="sheet">
  <header class="masthead">
    <div class="brand">HARLOW PENNY</div>
    <h1 class="doc-title">BASIC MONTHLY BUDGET</h1>
    <div class="period">
      <span>Month</span><div class="field month"></div>
      <span>Year</span><div class="field year"></div>
    </div>
  </header>

  <section class="ledger">
    <div class="ledger-head">
      <div class="col-head expense"><strong>Expenses (Category)</strong><span>Custom Category</span></div>
      <div class="col-head budget"><strong>Budget (USD)</strong><span>What you plan to spend</span></div>
      <div class="col-head actual"><strong>Actual (USD)</strong><span>What you actually spend</span></div>
    </div>
    <div class="ledger-rows">
      <div class="ledger-row"><div class="c-exp"></div><div class="c-bud"></div><div class="c-act"></div></div>
      <div class="ledger-row"><div class="c-exp"></div><div class="c-bud"></div><div class="c-act"></div></div>
      <div class="ledger-row"><div class="c-exp"></div><div class="c-bud"></div><div class="c-act"></div></div>
      <div class="ledger-row"><div class="c-exp"></div><div class="c-bud"></div><div class="c-act"></div></div>
      <div class="ledger-row"><div class="c-exp"></div><div class="c-bud"></div><div class="c-act"></div></div>
      <div class="ledger-row"><div class="c-exp"></div><div class="c-bud"></div><div class="c-act"></div></div>
      <div class="ledger-row"><div class="c-exp"></div><div class="c-bud"></div><div class="c-act"></div></div>
      <div class="ledger-row"><div class="c-exp"></div><div class="c-bud"></div><div class="c-act"></div></div>
      <div class="ledger-row"><div class="c-exp"></div><div class="c-bud"></div><div class="c-act"></div></div>
      <div class="ledger-row"><div class="c-exp"></div><div class="c-bud"></div><div class="c-act"></div></div>
      <div class="ledger-row"><div class="c-exp"></div><div class="c-bud"></div><div class="c-act"></div></div>
      <div class="ledger-row"><div class="c-exp"></div><div class="c-bud"></div><div class="c-act"></div></div>
      <div class="ledger-row"><div class="c-exp"></div><div class="c-bud"></div><div class="c-act"></div></div>
      <div class="ledger-row"><div class="c-exp"></div><div class="c-bud"></div><div class="c-act"></div></div>
      <div class="ledger-row"><div class="c-exp"></div><div class="c-bud"></div><div class="c-act"></div></div>
      <div class="ledger-row"><div class="c-exp"></div><div class="c-bud"></div><div class="c-act"></div></div>
      <div class="ledger-row"><div class="c-exp"></div><div class="c-bud"></div><div class="c-act"></div></div>
      <div class="ledger-row"><div class="c-exp"></div><div class="c-bud"></div><div class="c-act"></div></div>
    </div>
  </section>

  <footer class="formula-band">
    <div class="formula">
      <div class="term">
        <svg viewBox="0 0 50 50" aria-hidden="true"><circle cx="25" cy="25" r="25" fill="#fff"/><circle cx="25" cy="26" r="12" fill="var(--red)"/><rect x="21" y="11" width="8" height="3" rx="1" fill="var(--red)"/><text x="25" y="31" text-anchor="middle" font-family="Raleway,sans-serif" font-weight="700" font-size="14" fill="#fff">$</text></svg>
        <div><strong>Net Income</strong><span>How much money you kept</span></div>
      </div>
      <div class="operator">=</div>
      <div class="term">
        <svg viewBox="0 0 50 50" aria-hidden="true"><circle cx="25" cy="25" r="25" fill="#fff"/><path d="M20 12h10l-3 6c7 3 10 9 10 14 0 6-5 8-12 8s-12-2-12-8c0-5 3-11 10-14z" fill="var(--red)"/><text x="25" y="36" text-anchor="middle" font-family="Raleway,sans-serif" font-weight="700" font-size="15" fill="#fff">$</text></svg>
        <div><strong>Gross Income</strong><span>How much money you earned</span></div>
      </div>
      <div class="operator">–</div>
      <div class="term">
        <svg viewBox="0 0 50 50" aria-hidden="true"><circle cx="25" cy="25" r="25" fill="#fff"/><rect x="12" y="15" width="27" height="21" rx="2" fill="var(--red)"/><rect x="29" y="22" width="10" height="7" fill="#fff"/><circle cx="32" cy="25.5" r="1.5" fill="var(--red)"/><circle cx="15" cy="35" r="6" fill="var(--red)" stroke="#fff" stroke-width="1.5"/><rect x="12" y="34" width="6" height="2" fill="#fff"/></svg>
        <div><strong>Total Expenses</strong><span>Actual Expenses</span></div>
      </div>
    </div>
    <p class="visit">Visit us at harlowpenny.com for personal financial advice!</p>
  </footer>
</main>
</body>
</html>
```